Sleek and elegant promotional banner/sign for The Vellinor Law Firm

We need a design for promotional items like banners, signs, print ads, etc. that includes our firm name - "The Vellinor Law Firm" - and what we do. We advise businesses and individuals on legal matters; we represent individuals and businesses in litigation and transactions; we select and create business entities; we solve legal problems for individuals and businesses, etc. PLEASE DO NOT SIMPLY REPEAT THE PREVIOUS SENTENCE ON THE DESIGN. Please create a tag-line or brief description from ours. We need something that describes what we do in concise and creative manner while communicating trust and confidence. The banner must also include our basic contact information: 948.512-7740 (telephone) and vellinorlaw.com (website). You may use one or more of the attached images, but needn't use any with the right design. The design should be sleek and modern.

Target Market(s)

wealthy individuals and small business owners, entrepreneurs

Industry/Entity Type

Lawyer

Font styles to use
Sans Serif

Colors
33a6d7
0556a4
33b8a4

Requirements
Must have
• Firm name, contact information, BRIEF description of our services, sleek and elegant.
• Also, the design must be horizontal - not vertical.
Nice to have
• I'd like to use one of the images
Should not have
• Cliches

```html
<!DOCTYPE html>
<html lang="en">
<head>
<meta charset="utf-8">
<title>The Vellinor Law Firm – Banner</title>
<link href="https://fonts.googleapis.com/css2?family=Didact+Gothic&family=Questrial&family=Tinos:wght@400;700&display=swap" rel="stylesheet">
<style>
  :root {
    --page-bg: #ecedf1;
    --panel-white: #ffffff;
    --accent-cyan: #13b4ee;
    --accent-deep: #0556a4;
    --ink-dark: #4a4a4c;
    --ink-mid: #5a5a5c;
    --band-grey: #59595b;
    --photo-light: #7fb6d0;
    --photo-mid: #3f86aa;
    --photo-dark: #1d5878;
  }
  * { margin: 0; padding: 0; box-sizing: border-box; }
  html, body {
    width: 1200px; height: 862px; overflow: hidden;
    background: var(--page-bg);
  }
  .banner {
    position: absolute; left: 40px; top: 151px;
    width: 1120px; height: 560px; overflow: hidden;
    box-shadow: 0 6px 24px rgba(0,0,0,.18);
    background: var(--panel-white);
  }
  .banner-photo {
    position: absolute; left: 0; top: 0; width: 720px; height: 560px;
    background: radial-gradient(circle at 40% 75%, var(--photo-light) 0%, var(--photo-mid) 45%, var(--photo-dark) 100%);
  }
  .banner-shape { position: absolute; inset: 0; }
  .firm-name {
    position: absolute; right: 22px; top: 30px; text-align: right;
    font-family: "Didact Gothic", "Questrial", sans-serif;
    font-size: 68px; line-height: 66px; letter-spacing: 1px;
    color: var(--ink-dark); text-transform: uppercase;
  }
  .tagline-band {
    position: absolute; left: 620px; right: 0; top: 198px; height: 52px;
    background: var(--accent-cyan);
  }
  .tagline {
    position: absolute; right: 22px; top: 8px;
    font-family: "Questrial", sans-serif; font-size: 33px; color: #fff;
    white-space: nowrap;
  }
  .services { position: absolute; left: 690px; top: 262px; width: 420px; height: 130px; }
  .service {
    position: absolute; top: 0; width: 140px; text-align: center;
  }
  .service-icon { width: 92px; height: 92px; display: block; margin: 0 auto; }
  .service-label {
    margin-top: 10px;
    font-family: "Tinos", serif; font-size: 15px; line-height: 17px;
    letter-spacing: .5px; color: var(--ink-mid); text-transform: uppercase;
  }
  .phone {
    position: absolute; right: 16px; top: 408px;
    font-family: "Tinos", serif; font-size: 78px; line-height: 80px;
    color: var(--ink-dark); letter-spacing: 1px; white-space: nowrap;
  }
  .web-band {
    position: absolute; left: 585px; right: 0; top: 496px; height: 64px;
    background: var(--band-grey);
  }
  .website {
    position: absolute; right: 18px; top: 6px;
    font-family: "Tinos", serif; font-size: 44px; line-height: 50px;
    color: #fff; white-space: nowrap;
  }
</style>
</head>
<body>
  <div class="banner">
    <div class="banner-photo" role="img" aria-label="Photograph of blue interlocking jigsaw puzzle pieces arranged in concentric circles"></div>

    <svg class="banner-shape" width="1120" height="560" viewBox="0 0 1120 560" aria-hidden="true">
      <path d="M548 0 C580 120 620 215 672 282 C620 348 578 450 555 560 L1120 560 L1120 0 Z" fill="var(--accent-cyan)"/>
      <path d="M566 0 C598 120 638 215 690 282 C638 348 596 450 573 560" fill="none" stroke="var(--ink-dark)" stroke-width="2"/>
      <path d="M572 0 C604 120 644 215 696 282 C644 348 602 450 579 560 L1120 560 L1120 0 Z" fill="var(--panel-white)"/>
    </svg>

    <h1 class="firm-name">The Vellinor<br>Law Firm</h1>

    <div class="tagline-band"><p class="tagline">Legal Problems Solved</p></div>

    <div class="services">
      <div class="service" style="left:0">
        <svg class="service-icon" viewBox="0 0 92 92" aria-hidden="true">
          <circle cx="46" cy="46" r="46" fill="var(--accent-cyan)"/>
          <g fill="none" stroke="#fff" stroke-width="3.5" stroke-linecap="round">
            <line x1="46" y1="24" x2="46" y2="66"/>
            <line x1="26" y1="32" x2="66" y2="32"/>
            <line x1="34" y1="68" x2="58" y2="68"/>
            <path d="M26 32 L19 48 M26 32 L33 48 M66 32 L59 48 M66 32 L73 48"/>
          </g>
          <path d="M17 48 H35 A9 7 0 0 1 17 48 Z M57 48 H75 A9 7 0 0 1 57 48 Z" fill="#fff"/>
        </svg>
        <p class="service-label">Business<br>Litigation</p>
      </div>
      <div class="service" style="left:140px">
        <svg class="service-icon" viewBox="0 0 92 92" aria-hidden="true">
          <circle cx="46" cy="46" r="46" fill="var(--accent-cyan)"/>
          <g fill="#fff">
            <rect x="32" y="22" width="18" height="26" rx="2" transform="rotate(-40 41 35)"/>
            <rect x="46" y="38" width="7" height="30" transform="rotate(-40 49 53)"/>
            <rect x="22" y="64" width="28" height="8" rx="1"/>
          </g>
        </svg>
        <p class="service-label">Business<br>Law</p>
      </div>
      <div class="service" style="left:280px">
        <svg class="service-icon" viewBox="0 0 92 92" aria-hidden="true">
          <circle cx="46" cy="46" r="46" fill="var(--accent-cyan)"/>
          <rect x="24" y="20" width="44" height="52" rx="3" fill="#fff"/>
          <g fill="var(--accent-cyan)">
            <rect x="29" y="26" width="14" height="14"/>
            <rect x="48" y="26" width="14" height="5"/>
            <rect x="48" y="35" width="14" height="5"/>
            <rect x="29" y="46" width="33" height="5"/>
            <rect x="29" y="56" width="20" height="10"/>
          </g>
        </svg>
        <p class="service-label">Estate<br>Planning</p>
      </div>
    </div>

    <p class="phone">948.512-7740</p>

    <div class="web-band"><p class="website">www.vellinorlaw.com</p></div>
  </div>
</body>
</html>
```